Clean business card with logo provided

I want a card that will stand out among the masses. I need the color and image to show professionalism and yet have a family appeal showing that I only deal with win/win scenarios. The back of the card will be used to take notes about the individual so I can use that in my database entry. I like modern design but need professionalism in it also. It needs to fit my "clean, safe, and affordable housing" motto. I need to be able to write on the file and update the card details for my employees.

Target Market(s)

Investors looking to make investment income through real estate

Industry/Entity Type

Real Estate

Contact Information for Business Card

Troy Vandemark
blank address, city, st, zip code
480-555-0147
troyvandemark@quillrentals.example
www.quillrentals.example

Font styles to use
Sans Serif

Requirements
Must have
• I would like the back of the card to have lines for info. example
• Met/Visited: Date:
• Interets:
Nice to have
• I want the cards color to match the logo background color. Font with details to be san serif and black. I want the card rectangular with square corners. Standard business card size. I would like to see cards designed with both images to see which i prefer more.

```html
<!DOCTYPE html>
<html lang="en">
<head>
<meta charset="utf-8">
<title>Quill Rentals LLC – Business Card</title>
<link href="https://fonts.googleapis.com/css2?family=Lato:wght@400;700&display=swap" rel="stylesheet">
<style>
  :root {
    --page: #e9e6e1;
    --cyan: #0fc0d6;
    --cyan-deep: #06aec5;
    --black: #0c0c0c;
    --white: #ffffff;
    --shadow: rgba(0,0,0,0.28);
  }
  * { box-sizing: border-box; margin: 0; padding: 0; }
  html, body { width: 1200px; height: 1023px; overflow: hidden; }
  body {
    background: var(--page);
    font-family: "Lato", Arial, sans-serif;
    position: relative;
  }
  .card {
    position: absolute;
    width: 560px;
    height: 320px;
    box-shadow: 0 14px 30px var(--shadow);
    overflow: hidden;
  }
  .card-front {
    left: 70px; top: 110px;
    background: linear-gradient(135deg, #3fd3e4 0%, var(--cyan) 45%, var(--cyan-deep) 100%);
    color: var(--white);
  }
  .card-back {
    left: 570px; top: 590px;
    background: linear-gradient(160deg, #2a2a2a 0%, var(--black) 45%, #000 100%);
  }
  .edge-rule {
    position: absolute; top: 0; bottom: 0; right: 16px;
    width: 2px; background: var(--white);
  }
  .front-brand {
    position: absolute; left: 34px; top: 0; bottom: 0; width: 230px;
    display: flex; flex-direction: column; justify-content: center; align-items: center;
    text-align: center;
  }
  .brand-name {
    font-weight: 400; font-size: 34px; letter-spacing: 3px; line-height: 1;
  }
  .brand-sub {
    font-weight: 400; font-size: 13px; letter-spacing: 9px; margin-top: 8px;
  }
  .tagline {
    font-size: 10.5px; letter-spacing: 0.3px; margin-top: 8px;
  }
  .divider {
    position: absolute; left: 278px; top: 70px; height: 180px; width: 1.5px;
    background: rgba(255,255,255,0.85);
  }
  .contact {
    position: absolute; left: 300px; top: 74px; right: 30px;
  }
  .contact-name {
    font-weight: 700; font-size: 21px; font-variant: small-caps; letter-spacing: 0.5px;
    margin-bottom: 14px;
  }
  .contact-row {
    display: flex; align-items: center; gap: 8px;
    font-size: 12.5px; line-height: 1.9; white-space: nowrap;
  }
  .contact-row svg { width: 13px; height: 13px; flex: none; }
  .address { font-size: 13px; line-height: 1.55; margin-top: 6px; }
  .back-brand {
    position: absolute; inset: 0;
    display: flex; flex-direction: column; justify-content: center; align-items: center;
    color: var(--cyan);
    text-align: center;
  }
  .back-brand .brand-name { font-size: 46px; letter-spacing: 5px; }
  .back-brand .brand-sub { font-size: 15px; letter-spacing: 12px; margin-top: 10px; }
  .back-brand .tagline { font-size: 12px; margin-top: 10px; }
</style>
</head>
<body>
  <section class="card card-front" aria-label="Business card front">
    <div class="front-brand">
      <div class="brand-name">QUILL</div>
      <div class="brand-sub">RENTALS LLC</div>
      <div class="tagline">Providing clean, safe, and affordable housing</div>
    </div>
    <div class="divider"></div>
    <div class="contact">
      <div class="contact-name">Troy Vandemark</div>
      <div class="contact-row">
        <svg viewBox="0 0 16 16"><rect width="16" height="16" rx="3" fill="#1a1a1a"/><path d="M5 3.5l2 2-1 1.2a7 7 0 0 0 3.3 3.3l1.2-1 2 2-1.3 1.5C7.5 12.5 3.5 8.5 3.5 4.8z" fill="#fff"/></svg>
        <span>480-555-0147</span>
      </div>
      <div class="contact-row">
        <svg viewBox="0 0 16 16"><rect width="16" height="16" rx="3" fill="#1a1a1a"/><rect x="3" y="4.5" width="10" height="7" fill="none" stroke="#fff" stroke-width="1.2"/><path d="M3 4.5l5 4 5-4" fill="none" stroke="#fff" stroke-width="1.2"/></svg>
        <span>troyvandemark@quillrentals.example</span>
      </div>
      <div class="contact-row">
        <svg viewBox="0 0 16 16"><circle cx="8" cy="8" r="8" fill="#1a1a1a"/><circle cx="8" cy="8" r="4.6" fill="none" stroke="#fff" stroke-width="1.1"/><path d="M3.4 8h9.2M8 3.4c-2 2.5-2 6.7 0 9.2M8 3.4c2 2.5 2 6.7 0 9.2" fill="none" stroke="#fff" stroke-width="0.9"/></svg>
        <span>www.quillrentals.example</span>
      </div>
      <div class="address">00000 Harbor Blvd.<br>000 Marlow City, CA 00000</div>
    </div>
    <div class="edge-rule"></div>
  </section>

  <section class="card card-back" aria-label="Business card back">
    <div class="back-brand">
      <div class="brand-name">QUILL</div>
      <div class="brand-sub">RENTALS LLC</div>
      <div class="tagline">Providing clean, safe, and affordable housing</div>
    </div>
  </section>
</body>
</html>
```